General Power Point Presentation Pack

Hello Designers,

I am after a professional looking Microsoft PowerPoint deck that can be used for our corporate presentations. The pack should include a:

Title Page
Tittle and Content Page
Section Header Sheet
Two Content Page
Title Only Page
Blank Page
Content with Caption Page
Picture with Caption Page

I have included my brand guidelines and colours. I have also included some photos you may be able to use. Can you please ensure the pack has page numbering and that when you print it that it can be printed to full A4 Page.

Industry/Entity Type

Property Development & Construction

Requirements
Must have
• Prefer a white or very light coloured background

```html
<!DOCTYPE html>
<html lang="en">
<head>
<meta charset="utf-8">
<title>Corvale Presentation Pack</title>
<link href="https://fonts.googleapis.com/css2?family=Roboto:wght@300;400;500;700&display=swap" rel="stylesheet">
<style>
:root{
  --accent:#d9622b;
  --accent-soft:#f3d6c6;
  --ink:#222222;
  --muted:#8a8a8a;
  --line:#e6e6e6;
  --page:#f6f6f6;
  --card:#ffffff;
  --photo:linear-gradient(160deg,#cfd8e0 0%,#a59a8c 55%,#6f675c 100%);
  --photo-warm:linear-gradient(160deg,#e9e1d6 0%,#c9b49a 55%,#8f7a62 100%);
  --photo-sky:linear-gradient(180deg,#dfe7ee 0%,#c2ccd4 50%,#9aa3a8 100%);
}
*{box-sizing:border-box;margin:0;padding:0}
html,body{width:1200px;height:700px;overflow:hidden}
body{background:var(--page);font-family:'Roboto',sans-serif;color:var(--ink);position:relative}
.slide{position:absolute;width:228px;height:128px;background:var(--card);box-shadow:0 2px 6px rgba(0,0,0,.08);overflow:hidden}
.abs{position:absolute}
.slide-title{position:absolute;left:15px;top:12px;font-size:7.2px;font-weight:500;color:var(--ink)}
.slide-title::before{content:"";position:absolute;left:0;top:-4px;width:9px;height:1.2px;background:var(--accent)}
.brand{position:absolute;right:15px;top:13px;font-size:4.6px;font-weight:700;color:var(--accent);display:flex;align-items:center;gap:1.5px}
.brand::before{content:"";width:2.5px;height:2.5px;background:var(--accent)}
.foot{position:absolute;left:9px;bottom:6px;font-size:2.6px;color:var(--muted)}
.pg{position:absolute;right:10px;bottom:6px;font-size:2.6px;color:var(--muted)}
.photo{position:absolute;background:var(--photo)}
.photo.warm{background:var(--photo-warm)}
.tx{font-size:2.6px;line-height:1.45;color:#777}
.tx.c{text-align:center}
.hd{font-size:3.6px;font-weight:500;color:var(--ink)}
.pill{position:absolute;background:var(--accent);color:#fff;font-size:3.4px;border-radius:6px;text-align:center;line-height:7px;height:7px}
.box{position:absolute;background:var(--accent);color:#fff}
.cardw{position:absolute;background:#fff;box-shadow:0 1px 4px rgba(0,0,0,.12)}
.dot{position:absolute;width:16px;height:16px;border-radius:50%;background:var(--accent);box-shadow:0 0 0 2px var(--accent-soft)}
.cover-name{font-size:13px;font-weight:700;color:var(--accent)}
.cover-title{font-size:7px;font-weight:500;color:var(--ink)}
.cover-sub{font-size:2.8px;color:#555;line-height:1.6}
.toc-row{position:absolute;left:17px;width:78px;height:7px;font-size:2.6px;color:#999;border-bottom:.4px solid var(--line);display:flex;justify-content:space-between;align-items:center;padding:0 4px}
.toc-row.on{background:var(--accent);color:#fff;font-weight:500;border:none}
.num{font-size:7px;color:var(--accent);font-weight:500}
.hex{position:absolute;width:20px;height:22px;background:var(--accent);clip-path:polygon(50% 0,100% 25%,100% 75%,50% 100%,0 75%,0 25%);color:#fff;font-size:2.6px;display:flex;align-items:center;justify-content:center}
.iconrow{position:absolute;left:0;width:228px;height:10px}
</style>
</head>
<body>

<svg width="0" height="0" style="position:absolute">
  <defs>
    <symbol id="i-house" viewBox="0 0 10 10"><path d="M1 5 L5 1.5 L9 5 V9 H1 Z" fill="currentColor"/></symbol>
    <symbol id="i-pin" viewBox="0 0 10 10"><path d="M5 9 C2 5.5 2 4.5 2 4 A3 3 0 0 1 8 4 C8 4.5 8 5.5 5 9Z" fill="currentColor"/></symbol>
    <symbol id="i-tick" viewBox="0 0 10 10"><circle cx="5" cy="5" r="4" fill="none" stroke="currentColor" stroke-width="1.2"/><path d="M3 5 L4.5 6.5 L7 3.5" fill="none" stroke="currentColor" stroke-width="1.2"/></symbol>
    <symbol id="i-search" viewBox="0 0 10 10"><circle cx="4.3" cy="4.3" r="2.8" fill="none" stroke="currentColor" stroke-width="1.2"/><path d="M6.3 6.3 L9 9" stroke="currentColor" stroke-width="1.4"/></symbol>
    <symbol id="i-bars" viewBox="0 0 10 10"><rect x="1" y="5" width="2" height="4" fill="currentColor"/><rect x="4" y="3" width="2" height="6" fill="currentColor"/><rect x="7" y="1" width="2" height="8" fill="currentColor"/></symbol>
    <symbol id="i-phone" viewBox="0 0 10 10"><rect x="3" y="1" width="4" height="8" rx="1" fill="currentColor"/></symbol>
    <symbol id="i-person" viewBox="0 0 10 10"><circle cx="5" cy="3" r="2" fill="currentColor"/><path d="M1.5 9.5 C1.5 6 8.5 6 8.5 9.5Z" fill="currentColor"/></symbol>
    <symbol id="i-arrow" viewBox="0 0 10 10"><path d="M1 5 H8 M5.5 2.5 L8 5 L5.5 7.5" fill="none" stroke="currentColor" stroke-width="1.3"/></symbol>
  </defs>
</svg>

<!-- Row 1 -->
<section class="slide" style="left:9px;top:6px">
  <div class="abs cover-name" style="left:0;right:0;top:38px;text-align:center">Corvale</div>
  <div class="pill" style="left:89px;width:50px;top:63px">www.website.com</div>
  <div class="abs cover-title" style="left:0;right:0;top:78px;text-align:center">PRESENTATION TITTLE</div>
  <div class="abs cover-sub" style="left:0;right:0;top:88px;text-align:center">Here a Place for Credintial Presentation<br>June 2022</div>
</section>

<section class="slide" style="left:248px;top:6px">
  <div class="photo" role="img" aria-label="Faded photo of a modern apartment block" style="inset:0;opacity:.25"></div>
  <div class="abs" style="inset:0;background:linear-gradient(90deg,rgba(255,255,255,.2),rgba(255,255,255,.75) 30%,rgba(255,255,255,.75) 70%,rgba(255,255,255,.2))"></div>
  <div class="abs cover-name" style="left:0;right:0;top:38px;text-align:center">Corvale</div>
  <div class="pill" style="left:89px;width:50px;top:63px">www.website.com</div>
  <div class="abs cover-title" style="left:0;right:0;top:78px;text-align:center">PRESENTATION TITTLE</div>
  <div class="abs cover-sub" style="left:0;right:0;top:88px;text-align:center">Here a Place for Credintial Presentation<br>June 2022</div>
</section>

<section class="slide" style="left:486px;top:6px">
  <div class="photo" role="img" aria-label="Faded city street background" style="inset:0;opacity:.12"></div>
  <div class="abs" role="img" aria-label="Photo of tall glass residential towers" style="left:135px;top:25px;width:88px;height:103px;background:var(--photo-sky)"></div>
  <div class="abs cover-name" style="left:22px;top:40px">Corvale</div>
  <div class="abs cover-title" style="left:23px;top:62px">PRESENTATION TITTLE</div>
  <div class="abs cover-sub" style="left:23px;top:72px">Here a Place for Credintial Presentation<br>June 2022</div>
  <div class="pill" style="left:22px;width:50px;top:107px">www.website.com</div>
</section>

<section class="slide" style="left:725px;top:6px">
  <div class="slide-title">Content Page of CVL</div>
  <div class="toc-row" style="top:38px"><span>01. Section 1</span><span>01</span></div>
  <div class="toc-row on" style="top:48px;height:9px;font-size:3.2px"><span>02. Section 2</span><span>04</span></div>
  <div class="toc-row" style="top:62px"><span>03. Section 3</span><span>05</span></div>
  <div class="toc-row" style="top:74px"><span>04. Section 4</span><span>16</span></div>
  <div class="toc-row" style="top:86px"><span>05. Section 5</span><span>29</span></div>
  <div class="toc-row" style="top:98px"><span>06. End Section</span><span>35</span></div>
  <div class="photo" role="img" aria-label="Apartment building with timber facade" style="left:125px;top:0;width:103px;height:128px"></div>
  <div class="box" style="left:115px;top:57px;width:55px;height:14px;font-size:3px;display:flex;align-items:center;justify-content:center">Business Enhancement Plans</div>
  <div class="foot">Juny 2022</div>
</section>

<section class="slide" style="left:963px;top:6px">
  <div class="slide-title">Section Page</div>
  <div class="brand">Corvale</div>
  <div class="abs num" style="left:20px;top:36px">1</div>
  <div class="abs" style="left:28px;top:36px;width:80px"><div class="hd" style="font-size:2.8px">Section One</div><div class="tx">Short summary for this part of the deck goes here in two lines.</div></div>
  <div class="box" style="left:16px;top:54px;width:92px;height:20px"></div>
  <div class="abs num" style="left:20px;top:60px;color:#fff">2</div>
  <div class="abs" style="left:28px;top:59px;width:78px;color:#fff"><div style="font-size:2.8px;font-weight:500">Section Two</div><div class="tx" style="color:#fff">Short summary for this part of the deck goes here in two lines.</div></div>
  <div class="abs num" style="left:20px;top:86px">3</div>
  <div class="abs" style="left:28px;top:86px;width:80px"><div class="hd" style="font-size:2.8px">Section Three</div><div class="tx">Short summary for this part of the deck goes here in two lines.</div></div>
  <div class="abs num" style="left:121px;top:36px">4</div>
  <div class="abs" style="left:129px;top:36px;width:80px"><div class="hd" style="font-size:2.8px">Section Four</div><div class="tx">Short summary for this part of the deck goes here in two lines.</div></div>
  <div class="abs num" style="left:121px;top:60px">5</div>
  <div class="abs" style="left:129px;top:59px;width:80px"><div class="hd" style="font-size:2.8px">Section Five</div><div class="tx">Short summary for this part of the deck goes here in two lines.</div></div>
  <div class="abs num" style="left:121px;top:86px">6</div>
  <div class="abs" style="left:129px;top:86px;width:80px"><div class="hd" style="font-size:2.8px">Section Six</div><div class="tx">Short summary for this part of the deck goes here in two lines.</div></div>
  <div class="foot">Juny 2022</div><div class="pg">5</div>
</section>

<!-- Row 2 -->
<section class="slide" style="left:9px;top:145px">
  <div class="slide-title">About Our Company</div>
  <div class="brand">Corvale</div>
  <div class="photo" role="img" aria-label="Apartment block exterior" style="left:15px;top:33px;width:69px;height:37px"></div>
  <div class="photo" role="img" aria-label="Apartment block from the street" style="left:15px;top:72px;width:69px;height:36px"></div>
  <div class="abs" style="left:100px;top:41px;width:100px">
    <div class="tx" style="color:#444">Our team plans and builds quality homes across growing city districts.</div>
    <div class="tx" style="margin-top:3px">We guide every project from first sketch to handover, working with local partners, trusted trades and careful budgets so each site is delivered on time.</div>
    <div class="tx" style="margin-top:3px">New projects are opening across the region soon.</div>
  </div>
  <div class="abs tx" style="left:104px;top:87px;color:#444">56</div>
  <div class="abs tx" style="left:121px;top:87px;color:#444">$80K</div>
  <div class="box" style="left:138px;top:80px;width:20px;height:18px;font-size:3.4px;display:flex;align-items:center;justify-content:center">%87</div>
  <div class="foot">Juny 2022</div><div class="pg">6</div>
</section>

<section class="slide" style="left:248px;top:145px">
  <div class="slide-title">About Corvale</div>
  <div class="brand">Corvale</div>
  <div class="abs" style="left:18px;top:36px;width:88px">
    <div class="tx">We design and deliver homes that last. Each project is shaped by careful research, honest pricing and a team that stays on site until the keys are handed over.</div>
    <div class="tx" style="margin-top:3px">Growth is led by people who care about detail and quality work.</div>
  </div>
  <div class="cardw" style="left:18px;top:82px;width:30px;height:14px"><div style="color:var(--accent);font-size:4px;padding:2px 4px 0">+1055</div><div style="color:var(--accent);font-size:2.3px;padding-left:4px">Happy Costumer</div></div>
  <div class="box" style="left:51px;top:82px;width:30px;height:14px"><div style="font-size:4px;padding:2px 4px 0">+78</div><div style="font-size:2.3px;padding-left:4px">Costumer daily</div></div>
  <div class="photo" role="img" aria-label="Apartment building with green terraces" style="left:118px;top:35px;width:92px;height:66px"></div>
  <div class="foot">Juny 2022</div><div class="pg">7</div>
</section>

<section class="slide" style="left:486px;top:145px">
  <div class="slide-title">Our Vision</div>
  <div class="brand">Corvale</div>
  <div class="abs tx c" style="left:36px;right:36px;top:35px">We aim to shape liveable neighbourhoods with homes built for the long term, clear plans and a steady pace of growth across every district where we work today.</div>
  <div class="dot" style="left:27px;top:61px"></div>
  <div class="dot" style="left:89px;top:61px"></div>
  <div class="dot" style="left:151px;top:61px"></div>
  <svg class="abs" style="left:27px;top:61px" width="140" height="16" viewBox="0 0 140 16"><g color="#fff"><use href="#i-person" x="5" y="4" width="7" height="7"/><use href="#i-house" x="67" y="4" width="7" height="7"/><use href="#i-house" x="129" y="4" width="7" height="7"/></g></svg>
  <div class="abs" style="left:27px;top:82px;width:56px"><div class="hd">Vision One</div><div class="tx">Plans for growth set out how each team reaches its goals.</div></div>
  <div class="abs" style="left:89px;top:82px;width:56px"><div class="hd">Vision Two</div><div class="tx">Plans for growth set out how each team reaches its goals.</div></div>
  <div class="abs" style="left:151px;top:82px;width:56px"><div class="hd">Vision Three</div><div class="tx">Plans for growth set out how each team reaches its goals.</div></div>
  <div class="foot">Juny 2022</div><div class="pg">8</div>
</section>

<section class="slide" style="left:725px;top:145px">
  <div class="slide-title">Our Mission</div>
  <div class="brand">Corvale</div>
  <div class="abs tx c" style="left:25px;width:50px;top:36px"><div style="font-size:5px;color:#333">D</div><div style="color:#333;font-size:2.8px">Dicipline</div>Plans for growth help each team reach its daily goals.</div>
  <div class="box" style="left:85px;top:33px;width:56px;height:33px"></div>
  <div class="abs tx c" style="left:88px;width:50px;top:36px;color:#fff"><div style="font-size:5px">P</div><div style="font-size:2.8px">Productive</div>Plans for growth help each team reach its daily goals.</div>
  <div class="abs tx c" style="left:150px;width:50px;top:36px"><div style="font-size:5px;color:#333">E</div><div style="color:#333;font-size:2.8px">Educative</div>Plans for growth help each team reach its daily goals.</div>
  <div class="abs tx c" style="left:25px;width:50px;top:78px"><div style="font-size:5px;color:#333">G</div><div style="color:#333;font-size:2.8px">Globalism</div>Plans for growth help each team reach its daily goals.</div>
  <div class="abs tx c" style="left:88px;width:50px;top:78px"><div style="font-size:5px;color:#333">P</div><div style="color:#333;font-size:2.8px">Profit</div>Plans for growth help each team reach its daily goals.</div>
  <div class="abs tx c" style="left:150px;width:50px;top:78px"><div style="font-size:5px;color:#333">A</div><div style="color:#333;font-size:2.8px">Active</div>Plans for growth help each team reach its daily goals.</div>
  <div class="foot">Juny 2022</div><div class="pg">9</div>
</section>

<section class="slide" style="left:963px;top:145px">
  <div class="slide-title">Quote Page</div>
  <div class="brand">Corvale</div>
  <div class="box" style="left:23px;top:42px;width:183px;height:50px;box-shadow:0 2px 5px rgba(0,0,0,.15)"></div>
  <div class="abs" style="left:40px;top:59px;font-size:10px;font-weight:500;color:#fff">Quote</div>
  <div class="abs" style="left:86px;top:58px;width:112px;font-size:2.8px;line-height:1.5;color:#fff">“ Good homes start with honest plans, patient work and a team that keeps every promise made to the people who will live there. ”</div>
  <div class="foot">Juny 2022</div><div class="pg">10</div>
</section>

<!-- Row 3 -->
<section class="slide" style="left:9px;top:284px">
  <div class="slide-title">Leader Says</div>
  <div class="brand">Corvale</div>
  <div class="photo" role="img" aria-label="Portrait of the company leader" style="left:30px;top:37px;width:46px;height:53px;background:linear-gradient(180deg,#4a5a5a,#7a8a96 60%,#5f7a9a)"></div>
  <div class="abs" style="left:66px;top:56px;width:18px;height:18px;border-radius:50%;background:var(--accent);color:#fff;font-size:11px;font-weight:700;text-align:center;line-height:22px">“</div>
  <div class="abs" style="left:88px;top:57px;width:105px;font-size:3.4px;line-height:1.5;color:#444">We build for the families who will live in our homes, and we measure our success by how well each place serves them for years.</div>
  <div class="foot">Juny 2022</div><div class="pg">11</div>
</section>

<section class="slide" style="left:248px;top:284px">
  <div class="slide-title">Our Services</div>
  <div class="brand">Corvale</div>
  <div class="photo" role="img" aria-label="Apartment building behind palm trees" style="left:18px;top:38px;width:44px;height:50px"></div>
  <div class="photo warm" role="img" aria-label="Bright dining room interior" style="left:58px;top:52px;width:44px;height:50px"></div>
  <div class="box" style="left:44px;top:52px;width:20px;height:26px;font-size:3.4px;display:flex;align-items:center;justify-content:center">Plan A</div>
  <div class="abs" style="left:122px;top:40px;width:88px">
    <div class="tx">We offer design, planning and building under one roof, so clients deal with one team only.</div>
    <div class="hd" style="font-size:2.6px;margin-top:3px">Artchitech</div><div class="tx">Clear drawings and plans shape every new building we deliver.</div>
    <div class="hd" style="font-size:2.6px;margin-top:2px">Interior Design</div><div class="tx">Warm, simple rooms planned around the way people live.</div>
    <div class="hd" style="font-size:2.6px;margin-top:2px">Exterior Design</div><div class="tx">Facades and gardens that suit the street and the local area.</div>
  </div>
  <div class="foot">Juny 2022</div><div class="pg">12</div>
</section>

<section class="slide" style="left:486px;top:284px">
  <div class="slide-title">Our Strategy</div>
  <div class="brand">Corvale</div>
  <div class="photo" role="img" aria-label="Apartment complex with landscaped entry" style="left:22px;top:38px;width:87px;height:63px"></div>
  <div class="cardw" style="left:119px;top:38px;width:88px;height:64px"></div>
  <div class="box" style="left:119px;top:38px;width:88px;height:9px;font-size:3.6px;display:flex;align-items:center;justify-content:center">Marketing Startegy</div>
  <div class="abs" style="left:124px;top:51px;width:79px">
    <div class="tx">We reach buyers early with clear plans, open days and honest pricing across every new release.</div>
    <div class="tx" style="margin-top:3px">Sales teams follow each lead closely.</div>
    <div class="tx" style="margin-top:3px">Partners and agents share one plan so each launch stays on message.</div>
  </div>
  <div class="foot">Juny 2022</div><div class="pg">13</div>
</section>

<section class="slide" style="left:725px;top:284px">
  <div class="slide-title">Platinum Services</div>
  <div class="brand">Corvale</div>
  <div class="abs tx c" style="left:35px;right:35px;top:38px">Our premium service covers every step from land search to handover, with a single manager for each client and clear reports every week of the build.</div>
  <div class="box" style="left:20px;top:60px;width:42px;height:40px"></div>
  <div class="box" style="left:70px;top:60px;width:42px;height:40px"></div>
  <div class="box" style="left:120px;top:60px;width:42px;height:40px"></div>
  <div class="box" style="left:168px;top:60px;width:42px;height:40px"></div>
  <svg class="abs" style="left:20px;top:66px" width="190" height="8" viewBox="0 0 190 8"><g color="#fff"><use href="#i-person" x="17" y="0" width="7" height="7"/><use href="#i-house" x="67" y="0" width="7" height="7"/><use href="#i-arrow" x="117" y="0" width="7" height="7"/><use href="#i-bars" x="165" y="0" width="7" height="7"/></g></svg>
  <div class="abs tx c" style="left:20px;width:42px;top:80px;color:#fff"><b>Service One</b><br>Short line of text.</div>
  <div class="abs tx c" style="left:70px;width:42px;top:80px;color:#fff"><b>Service Two</b><br>Short line of text.</div>
  <div class="abs tx c" style="left:120px;width:42px;top:80px;color:#fff"><b>Service Three</b><br>Short line of text.</div>
  <div class="abs tx c" style="left:168px;width:42px;top:80px;color:#fff"><b>Service Four</b><br>Short line of text.</div>
  <div class="foot">Juny 2022</div><div class="pg">14</div>
</section>

<section class="slide" style="left:963px;top:284px">
  <div class="slide-title">Hexagraph</div>
  <div class="brand">Corvale</div>
  <div class="abs tx c" style="left:45px;right:45px;top:30px">Five steps guide each project from the first idea to the finished home, with each stage checked before the next one begins.</div>
  <svg class="abs" style="left:0;top:67px" width="228" height="2"><line x1="40" y1="1" x2="190" y2="1" stroke="#bbb" stroke-width=".5" stroke-dasharray="2 1.5"/></svg>
  <div class="hex" style="left:19px;top:57px">Info one</div>
  <div class="hex" style="left:61px;top:57px">Info Two</div>
  <div class="hex" style="left:101px;top:55px;width:24px;height:26px">Info Three</div>
  <div class="hex" style="left:144px;top:57px">Info Four</div>
  <div class="hex" style="left:185px;top:57px">Info Five</div>
  <div class="abs tx c" style="left:14px;width:30px;top:86px">Short note on this step.</div>
  <div class="abs tx c" style="left:56px;width:30px;top:86px">Short note on this step.</div>
  <div class="abs tx c" style="left:98px;width:30px;top:86px">Short note on this step.</div>
  <div class="abs tx c" style="left:139px;width:30px;top:86px">Short note on this step.</div>
  <div class="abs tx c" style="left:180px;width:30px;top:86px">Short note on this step.</div>
  <div class="foot">Juny 2022</div><div class="pg">15</div>
</section>

<!-- Row 4 -->
<section class="slide" style="left:9px;top:423px">
  <div class="slide-title">Analyse Company</div>
  <div class="brand">Corvale</div>
  <div class="abs tx c" style="left:35px;right:35px;top:38px">We review each market before we build, looking at demand, land prices and local plans so every project rests on solid ground.</div>
  <div class="abs" style="left:9px;top:65px;width:45px"><div class="hd" style="color:#555">Analyse One</div><div class="tx" style="margin-top:2px">1. Ways to profit management<br>2. Ways to Leadhership<br>3. Ways to team management<br>4. Ways to better future</div></div>
  <div class="box" style="left:55px;top:60px;width:49px;height:40px"></div>
  <div class="abs" style="left:61px;top:65px;width:45px;color:#fff"><div style="font-size:3.6px">Analyse Two</div><div class="tx" style="color:#fff;margin-top:2px">1. Ways to profit management<br>2. Ways to Leadhership<br>3. Ways to team management<br>4. Ways to better future</div></div>
  <div class="abs" style="left:113px;top:65px;width:45px"><div class="hd" style="color:#555">Analyse Three</div><div class="tx" style="margin-top:2px">1. Ways to profit management<br>2. Ways to Leadhership<br>3. Ways to team management<br>4. Ways to better future</div></div>
  <div class="abs" style="left:163px;top:65px;width:45px"><div class="hd" style="color:#555">Analyse Four</div><div class="tx" style="margin-top:2px">1. Ways to profit management<br>2. Ways to Leadhership<br>3. Ways to team management<br>4. Ways to better future</div></div>
  <div class="foot">Juny 2022</div><div class="pg">16</div>
</section>

<section class="slide" style="left:248px;top:423px">
  <div class="slide-title">Company Style</div>
  <div class="brand">Corvale</div>
  <div class="photo" role="img" aria-label="Apartment building with balconies" style="left:16px;top:42px;width:37px;height:48px"></div>
  <div class="photo" role="img" aria-label="Mid-rise building with planted terraces" style="left:58px;top:52px;width:37px;height:48px"></div>
  <svg class="abs" style="left:109px;top:45px" width="10" height="60" viewBox="0 0 10 60"><g color="#d9622b"><use href="#i-house" x="1" y="0" width="7" height="7"/><use href="#i-person" x="1" y="25" width="7" height="7"/><use href="#i-bars" x="1" y="50" width="7" height="7"/></g></svg>
  <div class="abs" style="left:123px;top:42px;width:90px"><div class="hd" style="font-size:2.8px">Property Profit</div><div class="tx">Each site is chosen for long term value and steady returns for our buyers.</div></div>
  <div class="abs" style="left:123px;top:67px;width:90px"><div class="hd" style="font-size:2.8px">Smart-Worker</div><div class="tx">Lean teams and clear tools keep every build moving on schedule.</div></div>
  <div class="abs" style="left:123px;top:92px;width:90px"><div class="hd" style="font-size:2.8px">Measureable</div><div class="tx">Progress is tracked weekly and shared openly with every client.</div></div>
  <div class="foot">Juny 2022</div><div class="pg">17</div>
</section>

<section class="slide" style="left:486px;top:423px">
  <div class="slide-title">Plan Company</div>
  <div class="brand">Corvale</div>
  <div class="photo" role="img" aria-label="Apartment blocks among trees" style="left:0;top:33px;width:82px;height:38px"></div>
  <div class="photo" role="img" aria-label="Apartment courtyard with palms" style="left:0;top:72px;width:82px;height:38px"></div>
  <div class="abs tx" style="left:90px;top:33px;width:120px">Our yearly plan sets clear goals for land, design, sales and delivery, with each team owning its part of the result.</div>
  <div class="abs" style="left:92px;top:57px;width:55px"><div class="hd" style="font-size:2.8px">Plan One</div><div class="tx">Short line about this plan step.</div></div>
  <div class="abs" style="left:92px;top:74px;width:55px"><div class="hd" style="font-size:2.8px">Plan Two</div><div class="tx">Short line about this plan step.</div></div>
  <div class="abs" style="left:92px;top:95px;width:55px"><div class="hd" style="font-size:2.8px">Plan Three</div><div class="tx">Short line about this plan step.</div></div>
  <div class="box" style="left:155px;top:64px;width:58px;height:20px"></div>
  <div class="abs" style="left:158px;top:67px;width:54px;color:#fff"><div style="font-size:2.8px">Plan Four</div><div class="tx" style="color:#fff">Short line about this plan step.</div></div>
  <div class="abs" style="left:155px;top:90px;width:55px"><div class="hd" style="font-size:2.8px">Plan Five</div><div class="tx">Short line about this plan step.</div></div>
  <div class="foot">Juny 2022</div><div class="pg">18</div>
</section>

<section class="slide" style="left:725px;top:423px">
  <div class="slide-title">Synergycal Company</div>
  <div class="brand">Corvale</div>
  <div class="photo warm" role="img" aria-label="Open plan living room interior" style="left:0;top:33px;width:92px;height:72px"></div>
  <div class="box" style="left:139px;top:34px;width:12px;height:12px"></div>
  <div class="box" style="left:200px;top:34px;width:12px;height:12px"></div>
  <div class="box" style="left:139px;top:72px;width:12px;height:12px"></div>
  <div class="box" style="left:200px;top:72px;width:12px;height:12px"></div>
  <svg class="abs" style="left:139px;top:34px" width="73" height="50" viewBox="0 0 73 50"><g color="#fff"><use href="#i-arrow" x="3" y="3" width="6" height="6"/><use href="#i-house" x="64" y="3" width="6" height="6"/><use href="#i-person" x="3" y="41" width="6" height="6"/><use href="#i-bars" x="64" y="41" width="6" height="6"/></g></svg>
  <div class="abs" style="left:102px;top:44px;width:50px"><div class="hd">Analyse One</div><div class="tx">Short note for this area of work.</div></div>
  <div class="abs" style="left:163px;top:44px;width:50px"><div class="hd">Analyse Two</div><div class="tx">Short note for this area of work.</div></div>
  <div class="abs" style="left:102px;top:82px;width:50px"><div class="hd">Analyse Three</div><div class="tx">Short note for this area of work.</div></div>
  <div class="abs" style="left:163px;top:82px;width:50px"><div class="hd">Analyse Four</div><div class="tx">Short note for this area of work.</div></div>
  <div class="foot">Juny 2022</div><div class="pg">19</div>
</section>

<section class="slide" style="left:963px;top:423px">
  <div class="slide-title">Company Strategy</div>
  <div class="brand">Corvale</div>
  <div class="abs" style="left:16px;top:37px;width:100px">
    <div class="tx">Our strategy balances growth with care, choosing sites close to work, schools and transport.</div>
    <div class="tx" style="margin-top:3px">We keep teams small, plans clear and costs open so buyers and partners can trust every number we share.</div>
    <div class="tx" style="margin-top:3px">New stages open each season.</div>
  </div>
  <div class="abs tx c" style="left:16px;top:90px;width:35px;color:#555">Happy Costumer<br>+1490</div>
  <div class="abs" style="left:52px;top:90px;width:.5px;height:8px;background:#ccc"></div>
  <div class="abs tx c" style="left:54px;top:90px;width:35px;color:#555">Done Project<br>+1382</div>
  <div class="photo" role="img" aria-label="Apartment facade" style="left:130px;top:29px;width:42px;height:41px"></div>
  <div class="box" style="left:172px;top:29px;width:42px;height:41px;font-size:3.6px;font-weight:500;display:flex;align-items:center;justify-content:center;text-align:center">Profit Plans<br>Company</div>
  <div class="box" style="left:130px;top:70px;width:42px;height:41px"></div>
  <svg class="abs" style="left:146px;top:85px" width="10" height="10"><use href="#i-house" width="10" height="10" color="#fff"/></svg>
  <div class="photo warm" role="img" aria-label="Dining room interior" style="left:172px;top:70px;width:42px;height:41px"></div>
  <div class="foot">Juny 2022</div><div class="pg">20</div>
</section>

<!-- Row 5 -->
<section class="slide" style="left:9px;top:562px">
  <div class="slide-title">Why Us?</div>
  <div class="brand">Corvale</div>
  <div class="photo" role="img" aria-label="Apartment complex in daylight" style="left:16px;top:41px;width:44px;height:60px"></div>
  <div class="photo" role="img" aria-label="Apartment tower close view" style="left:64px;top:41px;width:44px;height:60px"></div>
  <div class="box" style="left:96px;top:52px;width:37px;height:41px;font-size:3.4px;display:flex;align-items:center;padding-left:6px;line-height:1.5">Best Choise<br>Best Future</div>
  <div class="abs" style="left:144px;top:45px;width:72px;font-size:2.6px;line-height:1.45;font-weight:500;color:#333">We build homes people are proud of, with clear plans and honest prices from day one.</div>
  <div class="abs" style="left:144px;top:70px;font-size:5px;color:#444">2022</div>
  <div class="abs" style="left:160px;top:67px;width:56px"><div class="hd" style="font-size:2.6px">Preparation</div><div class="tx">Short note about this year.</div></div>
  <div class="abs" style="left:144px;top:90px;font-size:5px;color:#444">2023</div>
  <div class="abs" style="left:160px;top:87px;width:56px"><div class="hd" style="font-size:2.6px">Vendor Mapping</div><div class="tx">Short note about this year.</div></div>
  <div class="foot">Juny 2022</div><div class="pg">21</div>
</section>

<section class="slide" style="left:248px;top:562px">
  <div class="slide-title">Thank You</div>
  <div class="brand">Corvale</div>
  <div class="cardw" style="left:36px;top:38px;width:156px;height:70px"></div>
  <div class="abs" style="left:36px;width:156px;top:47px;text-align:center;font-size:3.2px;color:var(--accent)">STAY IN CONTACT WITH US</div>
  <div class="abs" style="left:62px;width:104px;top:53px;height:.4px;background:#ccc"></div>
  <div class="abs tx" style="left:79px;top:61px;color:#444"><span style="color:var(--accent)">Address</span><br>27 Ashby Lane<br>Eastbrook<br>Australia<br>Zip 40817</div>
  <div class="abs tx" style="left:121px;top:61px;color:#444"><span style="color:var(--accent)">Phone</span><br>555-014-2283<br><br><span style="color:var(--accent)">Email</span><br>hello@corvale.com</div>
  <div class="pill" style="left:89px;width:50px;top:104px">www.website.com</div>
  <div class="foot">Juny 2022</div><div class="pg">22</div>
</section>

<section class="slide" style="left:486px;top:562px">
  <div class="slide-title">Blank Page</div>
  <div class="brand">Corvale</div>
  <div class="foot">Juny 2022</div><div class="pg">23</div>
</section>

<section class="slide" style="left:725px;top:562px">
  <div class="slide-title">Icon Page</div>
  <div class="brand">Corvale</div>
  <svg class="iconrow" style="top:42px" viewBox="0 0 228 10"><g color="#d9622b">
    <use href="#i-arrow" x="36" width="6" height="6"/><use href="#i-house" x="48" width="6" height="6"/><use href="#i-phone" x="60" width="6" height="6"/><use href="#i-house" x="72" width="6" height="6"/><use href="#i-person" x="84" width="6" height="6"/><use href="#i-bars" x="96" width="6" height="6"/><use href="#i-tick" x="108" width="6" height="6"/><use href="#i-tick" x="120" width="6" height="6"/><use href="#i-pin" x="132" width="6" height="6"/><use href="#i-search" x="144" width="6" height="6"/><use href="#i-arrow" x="156" width="6" height="6"/><use href="#i-person" x="168" width="6" height="6"/><use href="#i-person" x="180" width="6" height="6"/></g></svg>
  <svg class="iconrow" style="top:58px" viewBox="0 0 228 10"><g color="#d9622b">
    <use href="#i-phone" x="36" width="6" height="6"/><use href="#i-bars" x="48" width="6" height="6"/><use href="#i-search" x="60" width="6" height="6"/><use href="#i-tick" x="72" width="6" height="6"/><use href="#i-search" x="84" width="6" height="6"/><use href="#i-house" x="96" width="6" height="6"/><use href="#i-arrow" x="108" width="6" height="6"/><use href="#i-bars" x="120" width="6" height="6"/><use href="#i-phone" x="132" width="6" height="6"/><use href="#i-search" x="144" width="6" height="6"/><use href="#i-bars" x="156" width="6" height="6"/><use href="#i-tick" x="168" width="6" height="6"/><use href="#i-arrow" x="180" width="6" height="6"/></g></svg>
  <svg class="iconrow" style="top:74px" viewBox="0 0 228 10"><g color="#d9622b">
    <use href="#i-house" x="36" width="6" height="6"/><use href="#i-tick" x="48" width="6" height="6"/><use href="#i-bars" x="60" width="6" height="6"/><use href="#i-pin" x="72" width="6" height="6"/><use href="#i-bars" x="84" width="6" height="6"/><use href="#i-phone" x="96" width="6" height="6"/><use href="#i-search" x="108" width="6" height="6"/><use href="#i-house" x="120" width="6" height="6"/><use href="#i-arrow" x="132" width="6" height="6"/><use href="#i-house" x="144" width="6" height="6"/><use href="#i-phone" x="156" width="6" height="6"/><use href="#i-tick" x="168" width="6" height="6"/><use href="#i-tick" x="180" width="6" height="6"/></g></svg>
  <svg class="iconrow" style="top:90px" viewBox="0 0 228 10"><g color="#d9622b">
    <use href="#i-bars" x="36" width="6" height="6"/><use href="#i-tick" x="48" width="6" height="6"/><use href="#i-house" x="60" width="6" height="6"/><use href="#i-search" x="72" width="6" height="6"/><use href="#i-house" x="84" width="6" height="6"/><use href="#i-phone" x="96" width="6" height="6"/><use href="#i-pin" x="108" width="6" height="6"/><use href="#i-arrow" x="120" width="6" height="6"/><use href="#i-pin" x="132" width="6" height="6"/><use href="#i-tick" x="144" width="6" height="6"/><use href="#i-pin" x="156" width="6" height="6"/><use href="#i-phone" x="168" width="6" height="6"/><use href="#i-arrow" x="180" width="6" height="6"/></g></svg>
  <div class="foot">Juny 2022</div><div class="pg">24</div>
</section>

<section class="slide" style="left:963px;top:562px">
  <div class="slide-title">Icon Page</div>
  <div class="brand">Corvale</div>
  <svg class="iconrow" style="top:42px" viewBox="0 0 228 10"><g color="#d9622b">
    <use href="#i-pin" x="38" width="5" height="5"/><use href="#i-bars" x="50" width="5" height="5"/><use href="#i-arrow" x="62" width="5" height="5"/><use href="#i-tick" x="74" width="5" height="5"/><use href="#i-search" x="86" width="5" height="5"/><use href="#i-tick" x="98" width="5" height="5"/><use href="#i-house" x="110" width="5" height="5"/><use href="#i-bars" x="122" width="5" height="5"/><use href="#i-phone" x="134" width="5" height="5"/><use href="#i-search" x="146" width="5" height="5"/><use href="#i-bars" x="158" width="5" height="5"/><use href="#i-arrow" x="170" width="5" height="5"/><use href="#i-house" x="182" width="5" height="5"/><use href="#i-tick" x="194" width="5" height="5"/></g></svg>
  <svg class="iconrow" style="top:56px" viewBox="0 0 228 10"><g color="#d9622b">
    <use href="#i-pin" x="38" width="5" height="5"/><use href="#i-tick" x="50" width="5" height="5"/><use href="#i-tick" x="62" width="5" height="5"/><use href="#i-phone" x="74" width="5" height="5"/><use href="#i-tick" x="86" width="5" height="5"/><use href="#i-person" x="98" width="5" height="5"/><use href="#i-bars" x="110" width="5" height="5"/><use href="#i-phone" x="122" width="5" height="5"/><use href="#i-bars" x="134" width="5" height="5"/><use href="#i-tick" x="146" width="5" height="5"/><use href="#i-phone" x="158" width="5" height="5"/><use href="#i-person" x="170" width="5" height="5"/><use href="#i-person" x="182" width="5" height="5"/></g></svg>
  <svg class="iconrow" style="top:72px" viewBox="0 0 228 10"><g color="#d9622b">
    <use href="#i-tick" x="38" width="5" height="5"/><use href="#i-phone" x="50" width="5" height="5"/><use href="#i-phone" x="62" width="5" height="5"/><use href="#i-house" x="74" width="5" height="5"/><use href="#i-bars" x="86" width="5" height="5"/><use href="#i-arrow" x="98" width="5" height="5"/><use href="#i-person" x="110" width="5" height="5"/><use href="#i-bars" x="122" width="5" height="5"/><use href="#i-bars" x="134" width="5" height="5"/><use href="#i-bars" x="146" width="5" height="5"/><use href="#i-search" x="158" width="5" height="5"/><use href="#i-phone" x="170" width="5" height="5"/><use href="#i-house" x="182" width="5" height="5"/></g></svg>
  <svg class="iconrow" style="top:88px" viewBox="0 0 228 10"><g color="#d9622b">
    <use href="#i-tick" x="38" width="5" height="5"/><use href="#i-arrow" x="50" width="5" height="5"/><use href="#i-tick" x="62" width="5" height="5"/><use href="#i-phone" x="74" width="5" height="5"/><use href="#i-person" x="86" width="5" height="5"/><use href="#i-tick" x="98" width="5" height="5"/><use href="#i-tick" x="110" width="5" height="5"/><use href="#i-tick" x="122" width="5" height="5"/><use href="#i-tick" x="134" width="5" height="5"/><use href="#i-person" x="146" width="5" height="5"/><use href="#i-phone" x="158" width="5" height="5"/><use href="#i-pin" x="170" width="5" height="5"/><use href="#i-tick" x="182" width="5" height="5"/></g></svg>
  <div class="foot">Juny 2022</div><div class="pg">25</div>
</section>

</body>
</html>
```